Chamomile Flower for Pet Birds

I need a label for a pet bird parrot supply company, new product, our first herb related product with more to come - company name is featherpantry.net - please visit and see logo and feel of our branding. Prefer the vertical label for this design. This particular product is designed to calm anxious and scared birds. Anxious, scared birds bite, feather pluck, have night frights, are afraid to be held and may become cage bound and mean.I'd like to see designs that strongly reflect the branding on the website which is colorful and fun yet modern and instills trust.

See competitions front label

Must include
Crude Protein (Min.) 1%
Crude Fat (Min.) 1%
Crude Fiber (Min.) 2%

Target Market(s)

Pet bird lovers who have birds that are anxious, screamers, biters or feather pickers

Industry/Entity Type

It Company

Font styles to use
Decorative

Requirements
Must have
• Must include
Crude Protein (Min.) 1%
Crude Fat (Min.) 1%
Crude Fiber (Min.) 2%

Logo & contact info

```html
<!DOCTYPE html>
<html lang="en">
<head>
<meta charset="utf-8">
<title>Chamomile Tea for Birds – Label Back</title>
<link rel="stylesheet" href="https://fonts.googleapis.com/css2?family=Arimo:wght@400;700&display=swap">
<style>
  :root {
    --paper: #ffffff;
    --ink: #1c1c1c;
    --petal: #fffbea;
    --bloom: #f7d44c;
    --bloom-deep: #f0a92e;
    --leaf: #3f9a3a;
    --sky: #1f8fc9;
    --berry: #d6336c;
  }
  * { margin: 0; padding: 0; box-sizing: border-box; }
  html, body {
    width: 753px;
    height: 1200px;
    overflow: hidden;
    background: var(--paper);
  }
  .label {
    position: relative;
    width: 753px;
    height: 1200px;
    background: var(--paper);
    color: var(--ink);
    font-family: "Arimo", Arial, sans-serif;
  }
  .flower-frame {
    position: absolute;
    inset: 0;
  }
  .info-panel {
    position: absolute;
    left: 84px;
    top: 64px;
    width: 592px;
    height: 1026px;
    border: 3px solid var(--leaf);
    border-radius: 14px;
    background: var(--paper);
    text-align: center;
    padding-top: 10px;
  }
  .section-title {
    font-size: 24px;
    font-weight: 700;
    line-height: 32px;
    color: var(--leaf);
  }
  .section-title.is-warning { color: var(--berry); }
  .section-title.is-analysis { color: var(--sky); }
  .section-body {
    font-size: 20.5px;
    font-weight: 700;
    line-height: 30px;
  }
  .brand-name {
    position: absolute;
    left: 0;
    right: 0;
    top: 1104px;
    text-align: center;
    font-size: 36px;
    font-weight: 700;
    letter-spacing: -0.5px;
    color: var(--sky);
  }
</style>
</head>
<body>
<div class="label">
  <svg class="flower-frame" width="753" height="1200" viewBox="0 0 753 1200" role="img" aria-label="Decorative border of chamomile daisy flowers framing the label">
    <defs>
      <linearGradient id="bloomTone" x1="0" y1="0" x2="1" y2="1">
        <stop offset="0" stop-color="#fff3b8"/>
        <stop offset="0.5" stop-color="#f7d44c"/>
        <stop offset="1" stop-color="#f0a92e"/>
      </linearGradient>
    </defs>
    <path fill="url(#bloomTone)" fill-rule="evenodd"
      d="M16 8 H740 V1194 H16 Z M80 60 H680 V1096 H700 V1150 H54 V1096 H80 Z"/>
  </svg>

  <section class="info-panel">
    <h2 class="section-title">Indications:</h2>
    <p class="section-body">Supports relief from anxious behaviors<br>such as plucking, self-mutilation, screaming,<br>biting, night frights.<br>Natural sedative helps eliminate<br>insomnia, anxiety &amp; stress.<br>Contains antibiotic properties,<br>relief for indigestion, muscle spasms.</p>

    <h2 class="section-title">Directions:</h2>
    <p class="section-body">Brew tea to leave in cage.<br>Change tea at least twice a day.<br>Always offer fresh water in addition to tea.<br>May spray cooled tea on feathers for<br>bird to ingest while preening.<br>Occasionally serve dried buds in dish<br>for bird to nibble on.</p>

    <h2 class="section-title is-warning">Warning:</h2>
    <p class="section-body">Always offer fresh water in addition<br>to Chamomile Tea;<br>Check with your Avian Veterinarian for<br>guidance regarding frequency and strength<br>of brew before incorporating<br>Chamomile Tea into your birds diet.</p>

    <h2 class="section-title">Storage:</h2>
    <p class="section-body">Store in a cool, dark, dry place away from humidity.</p>

    <h2 class="section-title">Ingredients:</h2>
    <p class="section-body">Egyptian Chamomile Flowers.<br>Gluten free ** Salt Free ** Sugar Free ** Vegan</p>

    <h2 class="section-title is-analysis">Guaranteed Analysis:</h2>
    <p class="section-body">Crude Protein (Min.) 1%<br>Crude Fat (Min.) 1%<br>Crude Fiber (Min.) 2%</p>
  </section>

  <div class="brand-name">featherpantry.net</div>
</div>
</body>
</html>
```